- Redesign our business card
- Logo remains unchanged
- Current business card attached

Target Market(s)

We are a property management company

Industry/Entity Type

Business

```html
<!DOCTYPE html>
<html lang="en">
<head>
<meta charset="utf-8">
<title>Harlow Property Group – Business Card</title>
<link rel="stylesheet" href="https://fonts.googleapis.com/css2?family=Cinzel:wght@400&family=Cormorant+Garamond:wght@400;500&display=swap">
<style>
  :root {
    --page: #f8f3e4;
    --ink-black: #000000;
    --charcoal: #3f3f3f;
    --sand: #e0d3ab;
    --white: #ffffff;
    --mist: #e5e5e7;
    --slate: #97979b;
    --rule: #8a8a8a;
    --text-dark: #1a1a1a;
  }
  * { margin: 0; padding: 0; box-sizing: border-box; }
  html, body { width: 1016px; height: 1200px; overflow: hidden; background: var(--page); }
  .canvas { position: relative; width: 1016px; height: 1200px; }

  .card { position: absolute; left: 40px; width: 923px; height: 560px; overflow: hidden; }

  /* Front */
  .card--front {
    top: 24px;
    background: linear-gradient(to bottom, var(--ink-black) 0%, #111 30%, #2c2c2c 62%, #1a1a1a 72%, var(--ink-black) 100%);
  }
  .brand {
    position: absolute; left: 0; right: 0; top: 405px;
    text-align: center; font-family: "Cinzel", serif; color: var(--white);
  }
  .brand__name {
    display: inline-flex; align-items: center; gap: 18px;
    font-size: 50px; letter-spacing: 1px; line-height: 1; color: var(--sand);
    transform: translateX(50px);
  }
  .brand__mark { width: 30px; height: 30px; background: var(--sand); }
  .brand__tagline {
    display: block; margin-top: 22px; font-size: 35px; line-height: 1;
    letter-spacing: 0.5px; transform: translateX(50px);
  }

  /* Back */
  .card--back { top: 609px; background: var(--mist); }
  .back__header {
    position: absolute; left: 0; top: 0; width: 100%; height: 252px;
    background: linear-gradient(to bottom, #111 0%, #2b2b2b 30%, #484848 50%, #2b2b2b 72%, #0d0d0d 100%);
    text-align: center; color: var(--white); font-family: "Cormorant Garamond", serif;
  }
  .person__name { position: absolute; left: 0; right: 0; top: 84px; font-size: 44px; font-weight: 500; line-height: 1; }
  .person__role { position: absolute; left: 0; right: 0; top: 136px; font-size: 23px; line-height: 1; }
  .services {
    position: absolute; left: 0; top: 252px; width: 100%; height: 45px;
    background: var(--ink-black); border-top: 3px solid var(--rule);
    display: flex; justify-content: space-between; align-items: center;
    padding: 0 38px 0 32px;
    font-family: "Cormorant Garamond", serif; font-size: 24px; color: var(--white);
  }
  .contact {
    position: absolute; left: 189px; top: 314px; list-style: none;
    font-family: "Cormorant Garamond", serif; font-size: 26px; font-weight: 500; color: var(--text-dark);
  }
  .contact li { height: 50px; line-height: 38px; }
  .web {
    position: absolute; left: 0; bottom: 0; width: 100%; height: 44px;
    background: var(--slate); color: var(--white); text-align: center;
    font-family: "Cormorant Garamond", serif; font-size: 25px; line-height: 44px;
  }
</style>
</head>
<body>
<main class="canvas">
  <section class="card card--front" aria-label="Card front">
    <div class="brand">
      <span class="brand__name"><span class="brand__mark"></span>HARLOW PROPERTY GROUP</span>
      <span class="brand__tagline">STRATA MANAGEMENT SERVICES</span>
    </div>
  </section>

  <section class="card card--back" aria-label="Card back">
    <header class="back__header">
      <h1 class="person__name">Daniel Harlow</h1>
      <p class="person__role">Licensed Strata Manager</p>
    </header>
    <nav class="services">
      <span>Strata Management</span>
      <span>Community Management</span>
      <span>Property Managment</span>
    </nav>
    <ul class="contact">
      <li>PO Box 48, Redfern Hills NSW 2016</li>
      <li>12/5-19 Marlow Street Ashbury NSW 2011</li>
      <li>T: 02 9384 1170 F: 02 9384 1175 M: 0431 608 279</li>
      <li>E: info@harlowproperty.com.au</li>
    </ul>
    <footer class="web">www.harlowproperty.com.au</footer>
  </section>
</main>
</body>
</html>
```